Escape Room Brochure, Trifold. Bold Black, yellow red. Doors Keys

We need a brochure to introduce our escape room and our services.
Attached are some of our designs as well as some examples of brochures we like.
We are THE VAULTS of KDW, however, we are aiming at Can you slip the vaults of KDW.
We are one of three escape rooms in a college town. We believe our rooms are more creative and original. Only family friendly. Brochure to be distributed to explain what an escape room is and promote our new fundraising program.

Font styles to use
Other font styles liked:
• impact

Colors
fbee3e
ec1f27
000000
dbdbdb

Requirements
Must have
• description of our rooms. services we offer. Fundraising and group teambuilding. Most information can be found at thevaultsofkdw.com
• what is an escape room.
Nice to have
• Photoshop
Should not have
• padlock or maze

```html
<!DOCTYPE html>
<html lang="en">
<head>
<meta charset="utf-8">
<title>The Vaults of KDW – Trifold Brochure</title>
<link rel="stylesheet" href="https://fonts.googleapis.com/css2?family=Anton&family=Varela+Round&display=swap">
<style>
:root{
  --yellow:#fbee3e;
  --red:#ec1f27;
  --black:#000000;
  --grey:#dbdbdb;
  --stage:#939598;
  --paper:#ffffff;
  --panel-light:#e9e9e9;
  --ink:#333333;
  --logo-grey:#c9c9c9;
}
*{box-sizing:border-box;margin:0;padding:0}
html,body{width:1138px;height:1200px;overflow:hidden}
body{background:var(--stage);position:relative;font-family:"Varela Round",sans-serif;color:var(--ink)}
.spread{position:absolute;left:42px;width:700px;height:540px;display:flex;box-shadow:0 2px 6px rgba(0,0,0,.35)}
.spread--outside{top:39px}
.spread--inside{top:625px}
.panel{position:relative;width:233.3px;height:540px;overflow:hidden}
.panel--black{background:var(--black);color:#fff}
.panel--white{background:var(--paper)}
.panel--light{background:var(--panel-light)}
.abs{position:absolute}
.stripe{position:absolute;left:0;width:100%;height:22px}
.photo{position:absolute}
.logo{font-family:"Varela Round",sans-serif;color:var(--logo-grey);text-transform:uppercase;line-height:1;letter-spacing:1px}
.logo .big{display:block;font-size:26px}
.logo .small{display:block;font-size:11px;text-align:right;letter-spacing:2px}
.tag-red{color:var(--red)}
.tag-yellow{color:var(--yellow)}
.body-copy{font-size:7.6px;line-height:1.4;color:#555}
.panel--black .body-copy{color:#fff}
.tab{position:absolute;left:12px;height:20px;background:var(--red);color:var(--yellow);font-size:12px;padding:3px 24px 0 10px;clip-path:polygon(0 0,82% 0,100% 100%,0 100%)}
.section-head{font-size:17px}
.live-escape{font-family:"Anton",sans-serif;text-align:right;line-height:.95;font-size:33px}
.live-escape .y{color:var(--yellow)}
.live-escape .r{color:var(--red)}
.url{font-size:10px;color:#fff}
.game{position:absolute;left:25px;display:flex;gap:8px;width:195px}
.game .thumb{flex:0 0 52px;height:52px;border-radius:50%}
.game p{font-size:7.4px;line-height:1.35;color:#fff}
.cover-card{position:absolute;width:233px;height:540px;background:var(--black);overflow:hidden;box-shadow:0 2px 6px rgba(0,0,0,.4)}
.door{position:absolute;background:linear-gradient(100deg,#111 0%,#2a2a2a 40%,#eeeeee 46%,#050505 52%,#000 100%)}
</style>
</head>
<body>

<section class="spread spread--outside">

  <article class="panel panel--white">
    <div class="photo" role="img" aria-label="Black and white collage of antique keys" style="left:0;top:0;width:233px;height:122px;background:radial-gradient(circle at 40% 50%,#cfcfcf,#5a5a5a 60%,#111)"></div>
    <svg class="stripe" style="top:112px;height:26px" viewBox="0 0 233 26" preserveAspectRatio="none"><polygon points="0,10 233,0 233,6 0,26" fill="var(--red)"/><polygon points="0,16 233,4 233,10 0,26" fill="var(--yellow)"/></svg>
    <h2 class="abs" style="left:16px;top:142px;font-size:15px;font-weight:400;color:#111;display:flex;align-items:baseline;gap:6px">Welcome to <span class="logo" style="color:#555"><span style="font-size:13px">The Vaults</span><span class="small" style="font-size:7px">of KDW</span></span></h2>
    <p class="abs body-copy" style="left:16px;top:183px;width:205px">We are a Kendwell, Texas based escape game experience with three rooms currently available and a fourth room on the way! We offer richly thematic escape rooms with great puzzles and mysteries relevant to each room. Our escape games are a great way to spend a weekend with 2 to 10 friends. Each escape room lasts about an hour, with varying difficulties and experiences.</p>
    <div class="abs" style="left:18px;top:283px;width:196px;height:76px;background:var(--yellow);border-radius:8px;font-size:7.4px;line-height:1.4;text-align:center;color:#111;padding:8px 8px">Our newest escape room, <b>'The Cellar of Shadows'</b> offers a heart-pounding and thrilling experience. Our goal is to provide an fun-filled hour that will keep groups tense and excited up until the final seconds.</div>
    <p class="abs body-copy" style="left:16px;top:377px;width:205px">We have something for any group here at The Vaults of KDW! Book online today, or contact us by phone. We are a local family-business, which makes us very prepared to work with you and your group to ensure you get the best experience possible. If you have any questions, especially if you want to book a party or special event at our business, call us at <b style="color:#111">877-2-ESC-KDW or (555)-014-7720!</b></p>
    <svg class="stripe" style="top:470px;height:32px" viewBox="0 0 233 32" preserveAspectRatio="none"><polygon points="0,24 233,0 233,8 0,32" fill="var(--red)"/><polygon points="80,18 233,4 233,12 80,26" fill="var(--yellow)"/></svg>
    <div class="abs" style="left:0;top:494px;width:233px;height:46px;background:var(--black);color:#fff;font-size:10px;padding:21px 0 0 19px">We look forward to hearing from you!</div>
  </article>

  <article class="panel panel--black" style="background:linear-gradient(180deg,#000 0%,#111 60%,#1c1c1c 100%)">
    <div class="abs" style="left:16px;top:86px;width:200px;text-align:center;font-size:8.8px;line-height:1.3;color:#fff">
      <span class="tag-yellow">Our current business hours are:</span><br>
      Monday through Thursday from 4:00 pm - 10:30 pm<br>
      Fridays from 3:00 pm - 11:30 pm<br>
      and Saturdays from 1:00 pm 11:30 pm<br>
      We are closed on Sundays, but if you would like to book u can contact us by phone at<br>
      <span class="tag-yellow">(555)-014-7720</span> or by email at hello@thevaultsofkdw.com, and we will do what we can to accomodate you.
    </div>
    <div class="abs tag-red" style="left:46px;top:307px;font-size:11px">CAN YOU ESCAPE?</div>
    <div class="abs logo" style="left:46px;top:321px"><span class="big" style="font-size:20px">The Vaults</span><span class="small">of KDW</span></div>
    <h3 class="abs tag-red" style="left:0;width:233px;text-align:center;top:374px;font-size:15px;font-weight:400">Contact Us</h3>
    <p class="abs" style="left:0;width:233px;text-align:center;top:403px;font-size:9.6px;line-height:1.4">4120 Harbor Ridge Road Suite 12,<br>Kendwell TX</p>
    <div class="abs tag-yellow" style="left:0;width:233px;text-align:center;top:440px;font-size:18px">(555) 014-7720</div>
    <div class="abs" style="left:0;width:233px;text-align:center;top:476px;font-size:9.5px">hello@thevaultsofkdw.com</div>
  </article>

  <article class="panel panel--black">
    <div class="door" role="img" aria-label="Half-open door with bright light spilling through" style="left:0;top:140px;width:233px;height:400px"></div>
    <div class="abs tag-red" style="left:25px;top:46px;font-size:15px">CAN YOU ESCAPE?</div>
    <div class="abs logo" style="left:25px;top:66px"><span class="big" style="font-size:28px">The Vaults</span><span class="small" style="font-size:13px">of KDW</span></div>
    <div class="abs live-escape" style="right:22px;top:388px"><span class="y">LIVE</span><br><span class="r">ESCAPE</span><br><span class="y">GAMES</span></div>
    <svg class="stripe" style="top:480px;height:40px" viewBox="0 0 233 40" preserveAspectRatio="none"><polygon points="70,30 233,16 233,24 70,38" fill="var(--red)"/><polygon points="110,24 233,12 233,18 110,30" fill="var(--yellow)"/></svg>
    <div class="abs" style="left:70px;top:512px;width:163px;height:28px;background:var(--black)"></div>
    <div class="abs url" style="right:25px;top:517px">www.thevaultsofkdw.com</div>
  </article>
</section>

<section class="spread spread--inside">

  <article class="panel panel--light">
    <div class="abs" style="left:0;top:0;width:233px;height:48px;background:var(--black)"></div>
    <h2 class="abs section-head tag-yellow" style="left:20px;top:14px;font-weight:400;font-size:15.5px">What is an Escape Room</h2>
    <svg class="stripe" style="top:40px;height:26px" viewBox="0 0 233 26" preserveAspectRatio="none"><polygon points="0,8 233,0 233,10 0,18" fill="var(--black)"/><polygon points="0,14 233,6 233,12 0,22" fill="var(--red)"/><polygon points="0,20 200,10 200,14 0,26" fill="var(--yellow)"/></svg>
    <p class="abs body-copy" style="left:22px;top:83px;width:195px">The Vaults of KDW is a <b style="color:#111">"real life"</b> escape game in which teams of 2-10 are locked in a deeply thematic room and given 1 hour to find their way out. By searching for clues, solving puzzles, and discovering the secrets each of our rooms have to offer, teams will attempt to beat the clock in this creative new form of entertainment.</p>
    <h2 class="abs section-head" style="left:20px;top:205px;font-weight:400;color:#111">Our Services</h2>
    <div class="tab" style="top:234px;left:18px">Parties</div>
    <div class="photo" role="img" aria-label="Group of friends in party hats celebrating" style="left:18px;top:254px;width:207px;height:99px;background:linear-gradient(120deg,#c49a7a,#e7c2a0 40%,#8aa0b8 70%,#5b6f85)"></div>
    <p class="abs" style="left:18px;top:359px;width:205px;font-size:7.6px;line-height:1.35;color:#111">At THE VAULTS of KDW we love to make your special events even more fun.</p>
    <p class="abs body-copy" style="left:18px;top:383px;width:205px;font-size:7.3px">The Vaults of KDW is a great place to have your next party or special event. We have a great area near the back of our business where you and your group can relax and have a nice celebration after your time in one or more of our escape rooms. We can comfortably fit up to 25 people for your party, and we can run multiple escape games at once. We would be happy to help you plan your party if you call us at (555)-014-7720 or e-mail us at hello@thevaultsofkdw.com.</p>
    <svg class="stripe" style="top:496px;height:24px" viewBox="0 0 233 24" preserveAspectRatio="none"><polygon points="0,10 233,0 233,8 0,18" fill="var(--red)"/><polygon points="0,16 233,6 233,12 0,22" fill="var(--yellow)"/></svg>
    <div class="abs" style="left:0;top:516px;width:233px;height:24px;background:var(--black)"></div>
  </article>

  <article class="panel panel--light" style="background:#eeeeee">
    <div class="tab" style="top:15px">Date Night</div>
    <div class="photo" role="img" aria-label="Smiling couple on a date" style="left:12px;top:35px;width:207px;height:90px;background:linear-gradient(110deg,#d8b28a,#f1d7b8 45%,#b88a63 75%,#e2e2e2)"></div>
    <p class="abs" style="left:12px;top:133px;width:210px;font-size:7.6px;line-height:1.35;color:#111">THE VAULTS Escape Games are the perfect place to enjoy a unique, one-of-a-kind experience together!</p>
    <p class="abs" style="left:12px;top:160px;font-size:7.6px;color:#111">THE PERFECT CHALLENGE FOR</p>
    <div class="abs body-copy" style="left:12px;top:178px;width:210px;font-size:6.3px;line-height:1.35">
      <p><b style="color:#111">The First Date:</b> A great way to break the ice and challenge yourself with each other! Nothing says "You're the coolest person I know!" more than taking your new girlfriend on a date to THE VAULTS Escape Games!</p>
      <p style="margin-top:6px"><b style="color:#111">The Third Date:</b> Show her you're committed by locking yourself in a room with her for 60 minutes and working together to find a way out!</p>
      <p style="margin-top:6px"><b style="color:#111">Anniversary:</b> Want a memorable experience that she isn't soon to forget? An experience that will have her talking to her friends and family about how great of a guy you really are?</p>
    </div>
    <div class="tab" style="top:295px">Team Building</div>
    <div class="photo" role="img" aria-label="Hands working together over puzzle pieces on a wooden table" style="left:12px;top:315px;width:207px;height:85px;background:linear-gradient(135deg,#5a4a3a,#8a7458 50%,#3e3228)"></div>
    <p class="abs body-copy" style="left:12px;top:409px;width:210px;font-size:7px">Escape games are well-known for being great for team-building. The escape room experience forces everyone in the room to work together, share information, and discuss problems in order to escape in time. They are an amazing option for co-workers looking to boost morale, promote teamwork, or just to create a nice ice-breaker situation that everyone will remember.</p>
    <div class="abs" style="left:0;top:516px;width:233px;height:24px;background:var(--black)"></div>
  </article>

  <article class="panel panel--black">
    <h2 class="abs section-head tag-yellow" style="left:25px;top:18px;font-weight:400;font-size:18px">Our Games</h2>
    <div class="game" style="top:53px">
      <div class="thumb" role="img" aria-label="Colourful retro pop-culture collage" style="background:radial-gradient(circle,#f2c230,#d23a2a 45%,#2d5fa8 75%,#111)"></div>
      <p>Our <b class="tag-yellow">'Retro Rewind'</b> escape game is fun for all ages. Families and groups of 90's kids have been enjoying this room since March 2016.</p>
    </div>
    <div class="game" style="top:127px">
      <div class="thumb" role="img" aria-label="Gloved hand against a blue laboratory backdrop" style="background:radial-gradient(circle,#dfe6f2,#6a7fb0 55%,#2a2f55)"></div>
      <p><b class="tag-yellow">'The Outbreak Lab'</b> escape room has been open since July 2016, and groups have been enjoying the extra challenge and complex medical/science themed clues.</p>
    </div>
    <p class="abs" style="left:24px;top:210px;width:180px;font-size:11.5px;line-height:1.35">We are also proud to announce that</p>
    <div class="game" style="top:256px;align-items:center">
      <div class="thumb" role="img" aria-label="Dim, eerie cellar corridor" style="background:radial-gradient(circle,#8a8578,#4a453d 55%,#1a1815)"></div>
      <p style="font-size:13.5px;line-height:1.3;color:var(--yellow)">The Cellar of Shadows is NOW OPEN.</p>
    </div>
    <p class="abs" style="left:21px;top:336px;width:200px;font-size:9.6px;line-height:1.4">Customers have been enjoying the scary, horror-movie style atmosphere!</p>
    <p class="abs" style="left:21px;top:373px;width:200px;font-size:9.6px;line-height:1.4">THE VAULTS of KDW is a family business. Ask about our new fundraising program for schools and clubs!</p>
    <div class="abs logo" style="left:47px;top:431px"><span class="big" style="font-size:22px">The Vaults</span><span class="small">of KDW</span></div>
    <svg class="stripe" style="top:480px;height:36px" viewBox="0 0 233 36" preserveAspectRatio="none"><polygon points="0,30 233,14 233,22 0,36" fill="var(--red)"/><polygon points="40,24 233,8 233,16 40,30" fill="var(--yellow)"/></svg>
    <div class="abs url" style="right:25px;top:516px">www.thevaultsofkdw.com</div>
  </article>
</section>

<div class="cover-card" style="left:832px;top:355px">
  <div class="door" role="img" aria-label="Half-open door with bright light spilling through" style="left:0;top:140px;width:233px;height:400px"></div>
  <svg class="stripe" style="top:480px;height:40px" viewBox="0 0 233 40" preserveAspectRatio="none"><polygon points="70,30 233,16 233,24 70,38" fill="var(--red)"/><polygon points="110,24 233,12 233,18 110,30" fill="var(--yellow)"/></svg>
  <div class="abs" style="left:70px;top:512px;width:163px;height:28px;background:var(--black)"></div>
  <div class="abs url" style="right:25px;top:517px">www.thevaultsofkdw.com</div>
</div>
<div class="cover-card" style="left:788px;top:310px">
  <div class="door" role="img" aria-label="Half-open door with bright light spilling through" style="left:0;top:140px;width:233px;height:400px"></div>
  <div class="abs tag-red" style="left:25px;top:46px;font-size:15px">CAN YOU ESCAPE?</div>
  <div class="abs logo" style="left:25px;top:66px"><span class="big" style="font-size:28px">The Vaults</span><span class="small" style="font-size:13px">of KDW</span></div>
  <div class="abs live-escape" style="right:25px;top:388px"><span class="y">LIVE</span><br><span class="r">ESCAPE</span><br><span class="y">GAMES</span></div>
  <svg class="stripe" style="top:480px;height:40px" viewBox="0 0 233 40" preserveAspectRatio="none"><polygon points="70,30 233,16 233,24 70,38" fill="var(--red)"/><polygon points="110,24 233,12 233,18 110,30" fill="var(--yellow)"/></svg>
  <div class="abs" style="left:70px;top:512px;width:163px;height:28px;background:var(--black)"></div>
  <div class="abs url" style="right:25px;top:517px">www.thevaultsofkdw.com</div>
</div>

</body>
</html>
```